Holiday Light Door Hanger

I need a new doorhanger design for our Holiday Light Service. I have attached our last one (which we DO like), but need to have a two-sided design. I also will attach photos that can be used as well as a FAQ about the service.

```html
<!DOCTYPE html>
<html lang="en">
<head>
<meta charset="utf-8">
<title>Holiday Light Door Hanger</title>
<link href="https://fonts.googleapis.com/css2?family=Poppins:wght@400;500;600;700;800&family=Yellowtail&display=swap" rel="stylesheet">
<style>
:root{
  --page:#ececec;
  --navy:#0b2170;
  --navy-deep:#061452;
  --navy-row:#123384;
  --green:#5cb82f;
  --green-bright:#6fd13a;
  --gold:#d9a441;
  --white:#ffffff;
  --night:#05091c;
}
*{margin:0;padding:0;box-sizing:border-box}
html,body{width:819px;height:1200px;overflow:hidden}
body{background:var(--page);font-family:'Poppins',sans-serif;color:var(--white);position:relative}
.hanger{position:absolute;top:100px;width:392px;height:1000px;overflow:hidden;
  background:linear-gradient(180deg,var(--navy-deep) 0%,var(--navy) 45%,var(--navy-deep) 100%);
  box-shadow:0 8px 22px rgba(0,0,0,.25)}
.hanger--front{left:12px}
.hanger--back{left:415px}
.art{position:absolute}
.center{position:absolute;left:0;width:100%;text-align:center}

/* front */
.front-garland{top:0;left:0;width:100%;height:250px;
  background:radial-gradient(circle at 15% 45%,rgba(217,164,65,.55),transparent 28%),
             radial-gradient(circle at 85% 45%,rgba(217,164,65,.55),transparent 28%),
             linear-gradient(180deg,rgba(250,230,120,.18),transparent 30%)}
.kicker{top:214px;font-size:8.5px;font-weight:700;letter-spacing:4px}
.script{top:234px;font-family:'Yellowtail',cursive;font-size:50px;line-height:1}
.headline{top:288px;font-weight:800;font-size:37px;line-height:1.02;letter-spacing:-.5px}
.headline .green{color:var(--green-bright);display:block}
.dots{top:370px;font-size:14px;color:var(--green-bright);letter-spacing:1px;line-height:1}
.intro{top:388px;left:38px;width:316px;font-size:9.4px;line-height:1.3;text-align:center}
.services-pill{position:absolute;top:504px;left:67px;width:258px;height:25px;border-radius:13px;
  background:var(--green);display:flex;align-items:center}
.services-pill .label{background:var(--white);color:var(--navy);font-weight:700;font-size:11px;
  height:25px;border-radius:13px;padding:0 11px;display:flex;align-items:center}
.services-pill .scope{font-size:8.8px;font-weight:600;padding-left:10px}
.service-list{position:absolute;top:545px;left:36px;width:320px;list-style:none}
.service-list li{height:26px;margin-bottom:3.2px;border-radius:13px;background:var(--navy-row);
  box-shadow:inset 0 -1px 0 rgba(255,255,255,.12);display:flex;align-items:center;justify-content:center;
  font-size:11.5px;font-weight:600}
.front-house{top:735px;left:0;width:100%;height:145px;
  background:radial-gradient(ellipse at 50% 70%,#c07a2a 0%,#5a2f14 35%,#16142a 70%,var(--navy-deep) 100%)}
.front-footer{position:absolute;top:880px;left:0;width:100%;height:120px;
  background:linear-gradient(180deg,#0a0c14,var(--night))}
.brand{display:flex;align-items:center;justify-content:center;gap:8px;font-weight:700;color:var(--white)}
.brand .mark{width:12px;height:12px;background:var(--green)}
.front-footer .brand{position:absolute;top:36px;left:0;width:100%;font-size:20px}

/* back */
.back-lights{top:0;left:0;width:100%;height:170px;
  background:radial-gradient(circle at 30% 30%,rgba(240,240,90,.25),transparent 40%),
             radial-gradient(circle at 75% 60%,rgba(240,240,90,.2),transparent 40%)}
.faq-title{top:196px;font-weight:800;font-size:28px;line-height:1.05;color:var(--green-bright)}
.faq-title .white{display:block;color:var(--white)}
.question-pill{position:absolute;top:262px;left:86px;width:220px;height:22px;border-radius:11px;
  background:var(--green);font-size:9.8px;font-weight:700;display:flex;align-items:center;justify-content:center}
.answer{top:292px;left:34px;width:324px;font-size:9.6px;line-height:1.25;text-align:center}
.clothesline{position:absolute;top:395px;left:0;width:100%;height:6px;background:#b98a55;transform:rotate(-1.5deg)}
.photo{position:absolute;background:var(--white);padding:5px;box-shadow:0 3px 8px rgba(0,0,0,.45)}
.photo .art{position:static;width:100%;height:100%}
.photo--1{top:400px;left:37px;width:103px;height:105px;transform:rotate(4deg)}
.photo--1 .art{background:linear-gradient(180deg,#1a2450,#5a3420)}
.photo--2{top:407px;left:145px;width:102px;height:100px}
.photo--2 .art{background:linear-gradient(180deg,#16338c,#2c4a8c 60%,#706a60)}
.photo--3{top:402px;left:252px;width:102px;height:104px;transform:rotate(-4deg)}
.photo--3 .art{background:radial-gradient(ellipse at 50% 50%,#8c6a4a,#101418 70%)}
.why{top:549px;left:40px;width:312px;font-size:10px;font-weight:700;line-height:1.3;color:var(--green-bright)}
.why-sub{top:577px;left:40px;width:312px;font-size:9.6px;line-height:1.25}
.features{position:absolute;top:612px;left:37px;width:316px;list-style:none}
.features li{display:flex;gap:8px;height:51px;padding:5px 0;border-bottom:1px dashed rgba(255,255,255,.4)}
.features li:last-child{border-bottom:none}
.features .icon{flex:0 0 30px;height:30px;background:var(--green);border-radius:3px;display:flex;align-items:center;justify-content:center}
.features h3{font-size:8.2px;font-weight:800;line-height:1.3}
.features h3 span{color:var(--green-bright)}
.features p{font-size:8px;line-height:1.25}
.back-barn{top:842px;left:0;width:168px;height:158px;
  background:linear-gradient(180deg,var(--navy) 0%,#3a4a7a 45%,#7a4a3a 75%,#1a2a5a 100%)}
.back-contact{position:absolute;top:846px;left:184px;width:204px}
.back-contact .brand{justify-content:flex-start;font-size:13px}
.back-contact h4{margin-top:24px;font-size:12px;font-weight:800}
.back-contact h4 span{color:var(--green-bright)}
.contact-list{list-style:none;margin-top:8px}
.contact-list li{display:flex;align-items:center;gap:4px;font-size:9.2px;font-weight:500;margin-bottom:5px;white-space:nowrap}
.contact-list svg{flex:0 0 8px}
</style>
</head>
<body>

<section class="hanger hanger--front">
  <div class="art front-garland" role="img" aria-label="String lights, gold ornaments and pine branches"></div>
  <p class="center kicker">ENJOY THE SEASON!</p>
  <p class="center script">Let us</p>
  <h1 class="center headline"><span class="green">HANDLE YOUR</span>LIGHTS!</h1>
  <p class="center dots">•••••</p>
  <p class="intro center">Our Holiday Lighting service can take the STRESS out of your holidays! We offer professionally designed, custom-cut lights for the roofline of your home or business! Additionally, we offer mini lights for shrubs and trees, wreaths, greenery and more! We will install your lights, service any issues throughout the season, remove them and store them for you for a year! Read on for some of the most common questions we get about our amazing service!</p>
  <div class="services-pill"><span class="label">OUR SERVICES</span><span class="scope">Residential &amp; Commercial</span></div>
  <ul class="service-list">
    <li>Custom Designed Displays</li>
    <li>Choice of Colors or Patterns</li>
    <li>Includes Design</li>
    <li>Installation</li>
    <li>Removal</li>
    <li>Storage and Maintenance</li>
  </ul>
  <div class="art front-house" role="img" aria-label="Brick house at night outlined with warm holiday lights"></div>
  <div class="front-footer">
    <div class="brand"><span class="mark"></span>Northfield Turf &amp; Outdoor</div>
  </div>
</section>

<section class="hanger hanger--back">
  <div class="art back-lights" role="img" aria-label="Glowing string lights across the top"></div>
  <h2 class="center faq-title">HOLIDAY LIGHTS<span class="white">FAQ</span></h2>
  <div class="question-pill">WHAT TYPE OF LIGHTS DO YOU USE?</div>
  <p class="answer center">We will furnish custom cut commercial lights in your choice of color or pattern, as well as all needed timers, extension cords or other accessories. Throughout the year we will return for any service issue to make sure your lights are rocking all season! Once the season is over, we will remove all lights, and safely store all items for the following season.</p>
  <div class="clothesline"></div>
  <figure class="photo photo--1"><div class="art" role="img" aria-label="Commercial building with roofline lights at night"></div></figure>
  <figure class="photo photo--2"><div class="art" role="img" aria-label="Lit walkway leading to a building at dusk"></div></figure>
  <figure class="photo photo--3"><div class="art" role="img" aria-label="Home outlined with white holiday lights"></div></figure>
  <p class="center why">WHY DO YOU ONLY OFFER LEASING INSTEAD OF SELLING LIGHTS?</p>
  <p class="center why-sub">Our lease-only model allows us to provide superior service and value</p>
  <ul class="features">
    <li>
      <span class="icon"><svg width="16" height="16" viewBox="0 0 18 18" fill="none" stroke="#fff" stroke-width="2" stroke-linecap="round"><path d="M3 3l12 12M15 3L3 15"/></svg></span>
      <div><h3>WORRY-FREE <span>MAINTENANCE</span></h3><p>Since we own the equipment, we're invested in keeping everything working perfectly. Any issues are resolved quickly at no cost to you.</p></div>
    </li>
    <li>
      <span class="icon"><svg width="16" height="16" viewBox="0 0 18 18" fill="none" stroke="#fff" stroke-width="2"><circle cx="9" cy="9" r="5"/><path d="M9 1v3M9 14v3M1 9h3M14 9h3"/></svg></span>
      <div><h3>ALWAYS CURRENT <span>TECHNOLOGY</span></h3><p>You get the latest commercial-grade LED technology each season, with automatic upgrades and replacements as needed</p></div>
    </li>
    <li>
      <span class="icon"><svg width="16" height="16" viewBox="0 0 18 18" fill="#fff"><path d="M9 2L1 8h2v8h12V8h2z"/><rect x="6" y="10" width="6" height="6" fill="#5cb82f"/></svg></span>
      <div><h3>ZERO STORAGE <span>HASSLES</span></h3><p>No cluttered garage or attic storage. We handle everything in our climate-controlled facility.</p></div>
    </li>
    <li>
      <span class="icon"><svg width="16" height="16" viewBox="0 0 18 18" fill="none" stroke="#fff" stroke-width="2"><rect x="3" y="5" width="12" height="11" rx="2"/><path d="M7 2h4M9 8v5"/></svg></span>
      <div><h3>PREDICTABLE <span>COSTS</span></h3><p>One annual fee covers everything - no surprise repair bills or replacement costs.</p></div>
    </li>
  </ul>
  <div class="art back-barn" role="img" aria-label="Barn outlined with holiday lights in the snow"></div>
  <div class="back-contact">
    <div class="brand"><span class="mark"></span>Northfield Turf &amp; Outdoor</div>
    <h4>CONTACT <span>US</span></h4>
    <ul class="contact-list">
      <li><svg width="8" height="8" viewBox="0 0 8 8"><circle cx="4" cy="4" r="4" fill="#5cb82f"/></svg>555.210.4480</li>
      <li><svg width="8" height="8" viewBox="0 0 8 8"><circle cx="4" cy="4" r="4" fill="#5cb82f"/></svg>hello@northfieldyard.com</li>
      <li><svg width="8" height="8" viewBox="0 0 8 8"><circle cx="4" cy="4" r="4" fill="#5cb82f"/></svg>140 Maple Ridge Rd, Fairview, IL 62900</li>
    </ul>
  </div>
</section>

</body>
</html>
```